Texas Civic Builders Summit Needs a Flyer

One-page event graphic/flyer and header needed. Logos provided.

2023 Texas Civic Builders Summit
Bold Ventures – True Accounts, True Answers, True Wins
August 10-11, 2023
San Antonio, Texas

About the Forum:
“Capital projects are full of risk. It’s not a question of eliminating risk, it’s a question of how to clearly identify it, reduce it, change it, or battle it.”
- Denise Holmgarten, Founder, U-BraMQ; San Antonio City Architect (retired)

Real Stories, Real Solutions, Real Success: U-BraMQ’s Texas Civic Builders Summit (TCBS) is designed to help you attain project success by hearing from Public Project Owners, architects, engineers, consultants, contractors, and suppliers. We are all in this together, and U-BraMQ is the organization that champions cross-collaboration and communication for project success!

For reference in design ONLY -
Here are some topic areas that bring project risks and/or rewards and that ultimately affect the Public Project Owner’s project success:

• Project Planning
• Regional Growth Shifts
• Project Funding
• Contracting
• Governmental Regulations
• Long-term COVID Impacts
• Infrastructure and Site Design
• Safety and Security
• Sustainability and Resilience
• Construction Predictability
• Leveraging Technology
• Facility Operations

Target Market(s)

Architects, Engineers, Contractors, project owners

Industry/Entity Type

Design and Construction

Requirements
Must have
• This is for a one-page (8.5x11) event graphic/flyer only - logos are provided. U-BraMQ logo, Texas Civic Builders Summit (TCBS) logo, 2023 Texas Civic Builders Summit, date, location
Nice to have
• Graphic(s) that represent the design and construction industry and the theme of this event (title, topics covered)
Should not have
• Full project description

```html
<!DOCTYPE html>
<html lang="en">
<head>
<meta charset="utf-8">
<title>2023 Texas Civic Builders Summit – Flyer</title>
<link href="https://fonts.googleapis.com/css2?family=Montserrat:wght@400;500;600;700;800&display=swap" rel="stylesheet">
<style>
  :root {
    --brand-blue: #17398f;
    --brand-green: #7cb342;
    --ink: #2a2a2a;
    --mark-grey: #555a60;
    --paper: #ffffff;
    --backdrop: #b5b5b5;
  }
  * { box-sizing: border-box; margin: 0; padding: 0; }
  html, body {
    width: 805px; height: 1200px; overflow: hidden;
    background: var(--backdrop);
    font-family: "Montserrat", sans-serif;
  }
  .canvas { position: relative; width: 805px; height: 1200px; overflow: hidden; }

  /* each page is built at 644 x 832 and scaled to fit the canvas */
  .page {
    position: absolute; left: 176px; width: 644px; height: 832px;
    background: var(--paper); overflow: hidden;
    transform: scale(0.702); transform-origin: top left;
    box-shadow: 0 4px 14px rgba(0,0,0,0.25);
  }
  .page-front { top: 10px; }
  .page-back { top: 606px; }
  .page-art { position: absolute; inset: 0; }

  .row { position: absolute; left: 0; width: 644px; text-align: center; white-space: nowrap; }

  /* ---------- front ---------- */
  .event-mark {
    position: absolute; top: 34px; left: 0; width: 644px;
    display: flex; flex-direction: column; align-items: center; gap: 5px;
  }
  .event-mark .dot { width: 12px; height: 12px; border-radius: 50%; background: var(--brand-blue); }
  .event-mark .name {
    color: var(--brand-blue); font-weight: 700; font-size: 20px;
    line-height: 1.15; text-align: center;
  }
  .headline-1 { top: 410px; font-weight: 800; font-size: 50px; line-height: 56px; color: var(--ink); }
  .headline-2 { top: 459px; font-weight: 800; font-size: 47px; line-height: 54px; color: var(--ink); }
  .accent { color: var(--brand-blue); }
  .theme {
    top: 522px; display: flex; justify-content: center; align-items: center; gap: 10px;
    color: var(--brand-green); font-weight: 800; font-size: 22px; line-height: 26px;
  }
  .theme::before, .theme::after { content: ""; width: 80px; height: 2px; background: var(--brand-blue); }
  .tagline { top: 549px; font-weight: 700; font-size: 18px; line-height: 22px; color: var(--ink); letter-spacing: 0.3px; }
  .date-month { top: 586px; color: var(--brand-blue); font-weight: 800; font-size: 26px; line-height: 30px; }
  .date-days { top: 607px; color: var(--ink); font-weight: 800; font-size: 52px; line-height: 60px; }
  .date-rule {
    position: absolute; top: 673px; left: 19px; width: 607px; height: 2px; background: var(--brand-green);
  }
  .date-rule::after {
    content: ""; position: absolute; left: 184px; top: -2px;
    width: 238px; height: 6px; border-radius: 3px; background: var(--brand-blue);
  }
  .location { top: 684px; font-weight: 700; font-size: 24px; line-height: 30px; color: var(--ink); }

  /* ---------- shared footer ---------- */
  .contact-pill {
    position: absolute; top: 736px; left: 263px; width: 118px; height: 24px;
    border-radius: 12px; background: var(--brand-green); color: var(--paper);
    font-weight: 700; font-size: 12px; display: flex; align-items: center; justify-content: center;
  }
  .contact-icons { position: absolute; top: 777px; left: 0; }
  .contact-line {
    top: 801px; display: flex; justify-content: center; align-items: center; gap: 12px;
    color: var(--paper); font-size: 11px; font-weight: 500; line-height: 18px;
  }
  .contact-line .phone { font-size: 14px; font-weight: 700; }
  .contact-line .sep { opacity: 0.7; }

  /* ---------- back ---------- */
  .section-pill {
    position: absolute; top: 20px; left: 57px; width: 530px; height: 43px;
    border-radius: 22px; background: var(--paper);
    display: flex; align-items: center; justify-content: center;
    font-size: 20px; font-weight: 500; color: var(--ink); letter-spacing: 0.3px;
  }
  .about {
    top: 80px; color: var(--paper); font-size: 12px; line-height: 15px; font-weight: 500;
  }
  .about b, .quote b { font-weight: 700; }
  .quote { top: 223px; color: var(--ink); font-size: 12px; line-height: 15px; font-weight: 500; }
  .quote-credit {
    position: absolute; top: 266px; left: 19px; width: 606px; height: 33px;
    border-radius: 16px; background: var(--brand-blue); color: var(--paper);
    display: flex; align-items: center; justify-content: center;
    font-size: 12px; font-weight: 700; letter-spacing: 0.2px;
  }
  .topics-intro { top: 333px; color: var(--paper); font-size: 16.5px; line-height: 20px; font-weight: 500; letter-spacing: 0.2px; }
  .topics-intro .accent { color: var(--brand-blue); }
  .topics-rule { position: absolute; top: 403px; left: 19px; width: 606px; height: 1px; background: var(--brand-blue); }
  .topics-rule::after {
    content: ""; position: absolute; left: 213px; top: -1px; width: 180px; height: 3px; background: var(--paper);
  }
  .topic-list { position: absolute; top: 414px; list-style: none; }
  .topic-list.col-a { left: 19px; }
  .topic-list.col-b { left: 331px; }
  .topic-list li {
    display: flex; align-items: center; gap: 6px;
    height: 23.2px; color: var(--paper); font-size: 12.5px; font-weight: 500; letter-spacing: 0.3px;
  }
  .topic-list li::before {
    content: ""; width: 10px; height: 10px; border-radius: 50%; background: var(--brand-blue); flex: none;
  }
  .org-name { top: 654px; font-size: 34px; line-height: 40px; font-weight: 600; color: var(--mark-grey); }
</style>
</head>
<body>
<div class="canvas">

  <!-- FRONT PAGE -->
  <section class="page page-front">
    <svg class="page-art" width="644" height="832" viewBox="0 0 644 832">
      <defs>
        <linearGradient id="dusk" x1="0" y1="0" x2="0" y2="1">
          <stop offset="0" stop-color="#e9a27d"/>
          <stop offset="0.25" stop-color="#7f88a8"/>
          <stop offset="0.5" stop-color="#3b4f73"/>
          <stop offset="0.75" stop-color="#4a77b5"/>
          <stop offset="1" stop-color="#1f3a5f"/>
        </linearGradient>
      </defs>
      <path role="img" aria-label="Photo: city skyline along a river at dusk" d="M0 0 H644 V340 Q322 446 0 340 Z" fill="url(#dusk)"/>
      <path d="M0 330 Q322 446 644 330 V372 Q322 428 0 372 Z" fill="var(--brand-blue)"/>
      <circle cx="323" cy="15" r="136" fill="#e3ddc3"/>
      <circle cx="323" cy="15" r="128" fill="var(--paper)"/>
      <path d="M0 783 Q322 693 644 783 V832 H0 Z" fill="var(--brand-green)"/>
      <path d="M0 808 Q322 714 644 808 V832 H0 Z" fill="var(--brand-blue)"/>
    </svg>

    <div class="event-mark">
      <span class="dot"></span>
      <p class="name">Texas Civic<br>Builders Summit</p>
    </div>

    <h1>
      <span class="row headline-1"><span class="accent">2023</span> Texas</span>
      <span class="row headline-2">Civic Builders <span class="accent">Summit</span></span>
    </h1>
    <p class="row theme">BOLD VENTURES</p>
    <p class="row tagline">True Accounts, True Answers, True Wins</p>
    <p class="row date-month">AUGUST</p>
    <p class="row date-days">10-11, 2023</p>
    <div class="date-rule"></div>
    <p class="row location">San Antonio, Texas</p>

    <div class="contact-pill">CONTACT US</div>
    <svg class="contact-icons" width="644" height="22" viewBox="0 0 644 22">
      <g fill="var(--paper)">
        <circle cx="148" cy="11" r="9"/><circle cx="322" cy="11" r="9"/><circle cx="497" cy="11" r="9"/>
      </g>
      <g fill="none" stroke="var(--brand-blue)" stroke-width="1.2">
        <rect x="143" y="7.5" width="10" height="7" rx="1"/><path d="M143 7.5 L148 12 L153 7.5"/>
        <path d="M318.5 6.5 q-1.5 2.5 1 5.5 q2.5 3 5.5 4 l1.5 -1.5 l-2.3 -1.6 l-1.1 .8 q-2.2 -1.1 -3 -3 l.8 -1.1 l-1.6 -2.3 Z"/>
        <circle cx="497" cy="11" r="5"/><ellipse cx="497" cy="11" rx="2.2" ry="5"/><path d="M492 11 H502"/>
      </g>
    </svg>
    <p class="row contact-line">
      <span>mara.feldt@u-bramq.org</span><span class="sep">|</span>
      <span class="phone">(512) 555-0147</span><span class="sep">|</span>
      <span>www.u-bramq.eventhub.org</span>
    </p>
  </section>

  <!-- BACK PAGE -->
  <section class="page page-back">
    <svg class="page-art" width="644" height="832" viewBox="0 0 644 832">
      <rect x="0" y="0" width="644" height="290" fill="var(--brand-blue)"/>
      <path d="M0 283 H644 V578 Q322 672 0 578 Z" fill="var(--brand-green)"/>
      <path d="M0 578 Q322 672 644 578 V605 Q322 659 0 605 Z" fill="var(--brand-blue)"/>
      <rect x="19" y="43" width="606" height="130" rx="16" fill="none" stroke="var(--brand-green)" stroke-width="2"/>
      <rect x="19" y="213" width="606" height="70" rx="16" fill="var(--paper)"/>
      <circle cx="321" cy="613" r="45" fill="var(--paper)"/>
      <circle cx="321" cy="613" r="37" fill="var(--brand-blue)"/>
      <path d="M0 783 Q322 693 644 783 V832 H0 Z" fill="var(--brand-green)"/>
      <path d="M0 808 Q322 714 644 808 V832 H0 Z" fill="var(--brand-blue)"/>
    </svg>

    <h2 class="section-pill">True Accounts, True Answers, True Wins</h2>
    <p class="row about">
      <b>U-BraMQ’s Texas Civic Builders Summit (TCBS)</b> is designed to help you attain<br>
      project success by hearing from Public Project Owners, architects, engineers,<br>
      consultants, contractors, and suppliers. We are all in this together,<br>
      and <b>U-BraMQ</b> is the organization that champions cross-collaboration and<br>
      communication for <b>Project Success</b> !
    </p>

    <p class="row quote">
      “Capital projects are full of risk. It’s not a question of eliminating risk,<br>
      it’s a question of how to clearly <b>identify it, reduce it, change it, or battle it</b>.”
    </p>
    <p class="quote-credit">Denise Holmgarten, Founder, U-BraMQ; San Antonio City Architect (retired)</p>

    <p class="row topics-intro">
      Here are some topic areas that bring<br>
      project risks and / or rewards and that ultimately affect<br>
      <span class="accent">The Public Project Owner’s project success</span>
    </p>
    <div class="topics-rule"></div>
    <ul class="topic-list col-a">
      <li>Project Planning</li>
      <li>Regional Growth Shifts</li>
      <li>Project Funding</li>
      <li>Contracting</li>
      <li>Governmental Regulations</li>
      <li>Long-term COVID Impacts</li>
    </ul>
    <ul class="topic-list col-b">
      <li>Infrastructure and Site Design</li>
      <li>Safety and Security</li>
      <li>Sustainability and Resilience</li>
      <li>Construction Predictability</li>
      <li>Leveraging Technology</li>
      <li>Facility Operations</li>
    </ul>

    <p class="row org-name">U-BraMQ</p>

    <div class="contact-pill">CONTACT US</div>
    <svg class="contact-icons" width="644" height="22" viewBox="0 0 644 22">
      <g fill="var(--paper)">
        <circle cx="148" cy="11" r="9"/><circle cx="322" cy="11" r="9"/><circle cx="497" cy="11" r="9"/>
      </g>
      <g fill="none" stroke="var(--brand-blue)" stroke-width="1.2">
        <rect x="143" y="7.5" width="10" height="7" rx="1"/><path d="M143 7.5 L148 12 L153 7.5"/>
        <path d="M318.5 6.5 q-1.5 2.5 1 5.5 q2.5 3 5.5 4 l1.5 -1.5 l-2.3 -1.6 l-1.1 .8 q-2.2 -1.1 -3 -3 l.8 -1.1 l-1.6 -2.3 Z"/>
        <circle cx="497" cy="11" r="5"/><ellipse cx="497" cy="11" rx="2.2" ry="5"/><path d="M492 11 H502"/>
      </g>
    </svg>
    <p class="row contact-line">
      <span>mara.feldt@u-bramq.org</span><span class="sep">|</span>
      <span class="phone">(512) 555-0147</span><span class="sep">|</span>
      <span>www.u-bramq.eventhub.org</span>
    </p>
  </section>

</div>
</body>
</html>
```